SnackHarbor!!! A Vending Machine Business Looking for an attractive website.

We are a vending machine business in Northern Michigan. We have changed our name and have rebranded our company. We would like an attractive website that shares who we are, what services we provide, the products we offer in our machines, along with a form businesses can fill out to see if they are a good fit for our company. I would like to have a Home Page, About SnackHarbor, Why Choose SnackHarbor?, Products & Services, Contact Us (With a Login Option), and a page with a questionnaire for thos interested in getting a FREE Vending Machine.

Target Market(s)

Businesses, Campgrounds, Schools, and many more in Northern Michigan

Industry/Entity Type

Vending Machines

Number of Pages Required

5+ page

Requirements
Must have
• An inviting and enticing Home Page. I want to get my potential clients engaged in our website.
Nice to have
• Possibly background photos from Northern Michigan
Should not have
• A corporate feel. I do not want a boring website.

```html
<!DOCTYPE html>
<html lang="en">
<head>
<meta charset="utf-8">
<title>SnackHarbor – Crave. Vend. Repeat</title>
<link href="https://fonts.googleapis.com/css2?family=Alfa+Slab+One&family=Poppins:wght@400;500;600;700&display=swap" rel="stylesheet">
<style>
:root{
  --navy:#1f2a6e;
  --navy-deep:#151d52;
  --green:#2c5a2b;
  --green-deep:#1f4520;
  --ink:#2a2f45;
  --muted:#6b7088;
  --paper:#ffffff;
  --mist:#eef1f6;
  --line:#c9cfdd;
}
*{box-sizing:border-box;margin:0;padding:0}
html,body{width:1200px;height:4252px;overflow:hidden}
body{position:relative;background:var(--paper);font-family:"Poppins",sans-serif;color:var(--ink)}
.abs{position:absolute}
.display{font-family:"Alfa Slab One",serif;font-weight:400;letter-spacing:1px;white-space:nowrap}
.eyebrow{font-size:18px;letter-spacing:3px;color:var(--navy);text-transform:uppercase;text-align:center}
.btn{display:inline-block;border-radius:30px;font-size:15px;font-weight:600;letter-spacing:1px;padding:14px 34px;text-transform:uppercase}
.btn-green{background:var(--green);color:#fff}
.btn-navy{background:var(--navy);color:#fff}
.btn-ghost{border:2px solid #fff;color:#fff}
.photo{border:none}

/* Header + hero */
.hero{left:0;top:0;width:1200px;height:660px;overflow:hidden}
.hero-bg{left:0;top:0;width:1200px;height:660px;background:linear-gradient(90deg,#fff 0%,#f3f5fa 38%,#3b4c8a 62%,#1a2456 100%)}
.brand{left:110px;top:22px;font-size:30px;color:var(--navy);font-weight:700;display:flex;align-items:center;gap:10px}
.brand-mark{width:22px;height:22px;background:var(--green);border-radius:4px}
.nav{left:520px;top:34px;display:flex;gap:38px;align-items:center}
.nav a{color:#fff;font-family:"Alfa Slab One",serif;font-size:13px;line-height:15px;text-decoration:none}
.nav .login{background:var(--green);padding:10px 22px;border-radius:4px;font-family:"Poppins",sans-serif;font-weight:700}
.hero-title{left:96px;top:238px;font-size:44px;color:var(--green);line-height:52px}
.hero-tag{left:96px;top:290px;font-size:36px;color:var(--navy);line-height:46px}
.hero-sub{left:100px;top:350px;font-size:22px;font-weight:600;color:var(--navy);line-height:28px}
.hero-btns{left:100px;top:426px;display:flex;gap:20px}
.hero-machine{left:720px;top:170px;width:380px;height:470px;border-radius:8px;background:linear-gradient(180deg,#d8dbe3,#8f95a6)}

/* About */
.about{left:0;top:660px;width:1200px;height:560px}
.about-bg{left:0;top:0;width:1200px;height:560px;background:linear-gradient(180deg,#ffffff 0%,#e7ecf4 55%,#b9c7d8 100%)}
.about .eyebrow{left:0;top:58px;width:1200px;font-size:15px}
.about h2{left:0;top:78px;width:1200px;text-align:center;font-size:40px;line-height:48px;color:var(--navy)}
.about h2 span{background:#fff;padding:0 14px}
.about-box{left:152px;top:102px;width:908px;height:300px;border:2px solid var(--line);border-radius:6px;background:rgba(255,255,255,.9)}
.about-box p{position:absolute;left:60px;top:88px;width:788px;text-align:center;font-size:17px;line-height:29px;color:var(--ink)}
.about-box .btn{position:absolute;left:386px;top:218px;padding:12px 32px;font-size:13px}

/* Why */
.why{left:0;top:1180px;width:1200px;height:720px}
.why h2{left:135px;top:156px;font-size:36px;line-height:44px;color:#fff}
.why .eyebrow{left:135px;top:128px;text-align:left;color:#dfe6d8;font-size:15px}
.why p{left:140px;width:460px;color:#eef3ea;font-size:16px;line-height:26px}
.why .btn{left:140px;top:470px}
.why-photo{left:660px;top:100px;width:520px;height:520px;border-radius:50%;background:radial-gradient(circle,#4a5d9c,#1e2a66);border:12px solid var(--navy)}

/* Products */
.products{left:0;top:1900px;width:1200px;height:640px}
.products .eyebrow{left:0;top:30px;width:1200px;font-size:15px}
.products h2{left:0;top:50px;width:1200px;text-align:center;font-size:44px;color:var(--navy)}
.card{top:150px;width:268px;height:420px;border:2px solid var(--line);border-radius:14px;background:#fff;text-align:center;overflow:hidden}
.card .machine{position:absolute;left:70px;top:30px;width:128px;height:210px;border-radius:6px;background:linear-gradient(180deg,#dfe2ea,#7d8398)}
.card h3{position:absolute;top:262px;width:100%;font-family:"Alfa Slab One",serif;font-weight:400;font-size:17px;color:var(--navy)}
.card p{position:absolute;left:30px;top:292px;width:208px;font-size:11px;line-height:16px;color:var(--muted)}
.card .btn{position:absolute;left:70px;top:352px;padding:10px 30px;font-size:12px}
.card.fade{opacity:.55}
.dots{left:540px;top:600px;display:flex;gap:8px}
.dots span{width:34px;height:4px;background:var(--line);border-radius:2px}
.dots span:first-child{background:var(--navy);width:50px}

/* Who */
.who{left:0;top:2560px;width:1200px;height:680px}
.who-bg{left:0;top:0;width:1200px;height:680px;background:linear-gradient(180deg,#fff 0%,#eef1f5 60%,#dfe6ee 100%)}
.who-photo{left:0;top:40px;width:560px;height:600px;background:linear-gradient(135deg,#a8b4c8,#5d6f94);border-radius:0 300px 300px 0;border-right:22px solid var(--green)}
.who .eyebrow{left:608px;top:120px;text-align:left;font-size:15px}
.who h2{left:606px;top:140px;font-size:44px;color:var(--navy)}
.who p{left:610px;width:500px;font-size:16px;line-height:26px;color:var(--ink)}
.who .btn{left:610px;top:560px}

/* Contact */
.contact-bg{left:0;top:3240px;width:1200px;height:740px;background:linear-gradient(180deg,#dfe6ee,#b8c6d6 60%,#eef1f5)}
.contact{left:140px;top:3280px;width:960px;height:660px;background:linear-gradient(180deg,var(--navy-deep),var(--navy));border-radius:30px;color:#fff}
.contact .eyebrow{left:0;top:64px;width:960px;color:#fff;font-size:15px}
.contact h2{left:0;top:84px;width:960px;text-align:center;font-size:44px;color:#fff}
.field{background:#fff;border-radius:4px;height:50px;color:var(--muted);font-size:15px;display:flex;align-items:center;gap:10px;padding-left:18px}
.field svg{flex:none}
.contact .btn{left:380px;top:570px;padding:13px 40px}

/* Footer */
.footer{left:0;top:3980px;width:1200px;height:272px;background:#fff}
.footer .brand-f{left:0;top:50px;width:1200px;display:flex;justify-content:center;align-items:center;gap:12px;font-size:40px;font-weight:700;color:var(--navy)}
.footer .brand-f span.sq{width:28px;height:28px;background:var(--green);border-radius:5px}
.foot-nav{left:0;top:150px;width:1200px;display:flex;justify-content:center;gap:30px;font-family:"Alfa Slab One",serif;font-size:15px;color:var(--navy)}
.foot-rule{left:130px;top:196px;width:940px;height:1px;background:var(--line)}
.copy{left:140px;top:222px;font-size:14px;color:var(--muted)}
.social{left:910px;top:218px;display:flex;gap:16px}
.social span{width:24px;height:24px;border-radius:50%;background:var(--navy)}
</style>
</head>
<body>

<section class="hero abs">
  <div class="hero-bg abs photo" role="img" aria-label="Evening view of a Northern Michigan town fading into a white hero backdrop"></div>
  <div class="brand abs"><span class="brand-mark"></span>SnackHarbor</div>
  <nav class="nav abs">
    <a>ABOUT<br>SNACKHARBOR</a>
    <a>WHY CHOOSE<br>SNACKHARBOR?</a>
    <a>PRODUCTS &amp;<br>SERVICES</a>
    <a>CONTACT<br>SNACKHARBOR</a>
    <a class="login">LOGIN</a>
  </nav>
  <h1 class="hero-title abs display">SNACKHARBOR!</h1>
  <div class="hero-tag abs display">CRAVE. VEND. REPEAT</div>
  <div class="hero-sub abs">ELEVATING SNACKING,<br>ONE VEND AT A TIME</div>
  <div class="hero-btns abs"><span class="btn btn-green">Learn More</span><span class="btn btn-navy">View Products</span></div>
  <div class="hero-machine abs photo" role="img" aria-label="Two stocked snack and drink vending machines"></div>
</section>

<section class="about abs">
  <div class="about-bg abs photo" role="img" aria-label="Faded aerial view of a Northern Michigan harbor"></div>
  <div class="about-box abs">
    <p>At SnackHarbor, we don't just vend snacks—we curate cravings. Our customized vending solutions bring flavor, convenience, and community to Northern Michigan. Whether you're reaching for a mid-morning snack, a refreshing beverage, or a satisfying breakfast burrito, SnackHarbor delivers delight with every bite.</p>
    <span class="btn btn-navy">Learn More</span>
  </div>
  <div class="eyebrow abs">Our Company</div>
  <h2 class="abs display"><span>ABOUT SNACKHARBOR!</span></h2>
</section>

<section class="why abs">
  <svg class="abs" style="left:0;top:0" width="1200" height="720" viewBox="0 0 1200 720">
    <path d="M0 100 Q600 -20 1200 90 L1200 640 Q600 760 0 620 Z" fill="var(--navy)"/>
    <path d="M0 120 Q600 10 1200 110 L1200 620 Q600 730 0 600 Z" fill="var(--green)"/>
  </svg>
  <div class="eyebrow abs">Why Choose Us</div>
  <h2 class="abs display">WHY SNACKHARBOR ?</h2>
  <p class="abs" style="top:224px">At SnackHarbor, we're more than vending machines; we're flavor architects, community connectors, and taste trailblazers. Imagine a world where every snack is an adventure, every sip a celebration. That's the SnackHarbor promise—a symphony of taste, convenience, and camaraderie.</p>
  <p class="abs" style="top:400px">Our Tailored Temptations await: from salty to sweet, our snack selection dances with variety.</p>
  <span class="btn btn-ghost abs">Learn More</span>
  <div class="why-photo abs photo" role="img" aria-label="Three vending machines against a town backdrop"></div>
</section>

<section class="products abs">
  <div class="eyebrow abs">What We Offer</div>
  <h2 class="abs display">OUR PRODUCTS!</h2>
  <div class="card abs" style="left:90px"><div class="machine photo" role="img" aria-label="Drink vending machine"></div><h3>VENDOR MACHINE</h3><p>Fresh snacks and cold drinks, stocked daily.</p><span class="btn btn-green">Learn More</span></div>
  <div class="card abs" style="left:392px"><div class="machine photo" role="img" aria-label="Snack vending machine"></div><h3>VENDOR MACHINE</h3><p>Fresh snacks and cold drinks, stocked daily.</p><span class="btn btn-green">Learn More</span></div>
  <div class="card abs" style="left:688px"><div class="machine photo" role="img" aria-label="Combo vending machine"></div><h3>VENDOR MACHINE</h3><p>Fresh snacks and cold drinks, stocked daily.</p><span class="btn btn-green">Learn More</span></div>
  <div class="card fade abs" style="left:980px"><div class="machine photo" role="img" aria-label="Snack vending machine"></div><h3>VENDOR MACHINE</h3><p>Fresh snacks and cold drinks, stocked daily.</p><span class="btn btn-green">Learn More</span></div>
  <div class="dots abs"><span></span><span></span><span></span></div>
</section>

<section class="who abs">
  <div class="who-bg abs photo" role="img" aria-label="Faded Northern Michigan townscape"></div>
  <div class="who-photo abs photo" role="img" aria-label="Hand paying at a vending machine keypad"></div>
  <div class="eyebrow abs">SnackHarbor</div>
  <h2 class="abs display">WHO WE ARE!</h2>
  <p class="abs" style="top:222px">We're not just about vending machines; we're your culinary companions, your flavor curators,</p>
  <p class="abs" style="top:290px">and your secret stash of happiness. We're the ones who believe that a vending machine isn't just a metal box; it's a portal to delight.</p>
  <p class="abs" style="top:386px">Our mission? To transform mundane moments into memorable bites. Daniel and Nora, the dynamic duo behind SnackHarbor, have a passion for all things tasty. With backgrounds in sales and a penchant for personal connections, they've transformed the vending experience into an art form.</p>
  <span class="btn btn-navy abs">Learn More</span>
</section>

<div class="contact-bg abs photo" role="img" aria-label="Faded waterfront view of a Northern Michigan harbor"></div>
<section class="contact abs">
  <div class="eyebrow abs">Get In Touch</div>
  <h2 class="abs display">CONTACT US!</h2>
  <div class="field abs" style="left:100px;top:190px;width:370px"><svg width="16" height="16" viewBox="0 0 16 16"><circle cx="8" cy="5" r="3.5" fill="var(--navy)"/><path d="M1 16c0-4 3-6 7-6s7 2 7 6z" fill="var(--navy)"/></svg>First Name</div>
  <div class="field abs" style="left:490px;top:190px;width:370px"><svg width="16" height="16" viewBox="0 0 16 16"><circle cx="8" cy="5" r="3.5" fill="var(--navy)"/><path d="M1 16c0-4 3-6 7-6s7 2 7 6z" fill="var(--navy)"/></svg>Last Name</div>
  <div class="field abs" style="left:100px;top:262px;width:370px"><svg width="16" height="14" viewBox="0 0 16 14"><rect x="1" y="1" width="14" height="12" rx="1" fill="none" stroke="var(--navy)" stroke-width="2"/><path d="M1 2l7 6 7-6" fill="none" stroke="var(--navy)" stroke-width="2"/></svg>Email address</div>
  <div class="field abs" style="left:490px;top:262px;width:370px"><svg width="16" height="16" viewBox="0 0 16 16"><path d="M3 1l3 3-2 2c1 2 3 4 6 6l2-2 3 3-2 3C7 16 0 9 0 3z" fill="var(--navy)"/></svg>Phone</div>
  <div class="field abs" style="left:100px;top:334px;width:760px;height:180px;align-items:flex-start;padding-top:16px"><svg width="16" height="16" viewBox="0 0 16 16"><path d="M1 1h14v10H5l-4 4z" fill="var(--navy)"/></svg>Message</div>
  <span class="btn btn-ghost abs">Send Message</span>
</section>

<footer class="footer abs">
  <div class="brand-f abs"><span class="sq"></span>SnackHarbor</div>
  <div class="foot-nav abs"><span>HOME</span><span>•</span><span>ABOUT SNACKHARBOR</span><span>•</span><span>WHY CHOOSE SNACKHARBOR?</span><span>•</span><span>PRODUCTS &amp; SERVICES</span><span>•</span><span>CONTACT US</span></div>
  <div class="foot-rule abs"></div>
  <div class="copy abs">Copyright © 2024 SnackHarbor. All rights reserved.</div>
  <div class="social abs"><span></span><span></span><span></span><span></span></div>
</footer>

</body>
</html>
```